Harborlane Venture Primer needs a cover!

We have written an book containing information on how a foreigner can open a business in Brazil. We start from basic facts about life and culture and we go up to details of visa requirements, tax issues and the employment law. The audience is people excited about the prospects of moving to a new, up and coming place to start a new life. The final book title is most likely going to be "Harborlane Venture Primer 2014". We want a dynamic and optimistic design which can be used for both the ebook and the later print version. The colors are likely to be greens, blue, yellow as in the Brazilian flag. It would be ideal to have a design that is clearly understood even when in thumbnail format and that will attract interest.

```html
<!DOCTYPE html>
<html lang="en">
<head>
<meta charset="utf-8">
<title>Harborlane Venture Primer 2014 — Cover</title>
<link rel="stylesheet" href="https://fonts.googleapis.com/css2?family=Anton&family=Open+Sans:wght@400;600&display=swap">
<style>
  :root {
    --flag-green: #00883f;
    --flag-yellow: #f7c100;
    --flag-navy: #271a6e;
    --paper: #ffffff;
    --sky-pale: #dfeef5;
    --sky-mid: #9cc4d8;
    --sky-deep: #6c9fb8;
    --grass-light: #7cc243;
    --grass-deep: #3f8a1f;
  }
  * { margin: 0; padding: 0; box-sizing: border-box; }
  html, body { width: 927px; height: 1200px; overflow: hidden; background: var(--paper); }
  .cover { position: relative; width: 927px; height: 1200px; overflow: hidden; background: var(--paper); }
  .cover-photo {
    position: absolute; inset: 0;
    background: linear-gradient(180deg,
      var(--paper) 0%, var(--paper) 22%,
      var(--sky-pale) 34%, var(--sky-mid) 50%, var(--sky-deep) 62%,
      var(--sky-pale) 80%, var(--grass-light) 81%, var(--grass-deep) 100%);
  }
  .cover-art { position: absolute; inset: 0; width: 927px; height: 1200px; }
  .title-line { font-family: "Anton", "Impact", sans-serif; }
  .title-line--harbor { fill: var(--flag-green); }
  .title-line--venture { fill: var(--flag-yellow); }
  .title-line--primer { fill: var(--flag-navy); stroke: var(--paper); stroke-width: 4px; paint-order: stroke; }
  .flag-block { fill: var(--flag-green); }
  .blurb {
    position: absolute; left: 44px; top: 1058px; width: 850px;
    font-family: "Open Sans", sans-serif; font-size: 15.5px; line-height: 23px;
    letter-spacing: 0.6px; color: var(--paper);
  }
  .blurb-lead { font-size: 26px; letter-spacing: 0.5px; }
  .author {
    position: absolute; right: 58px; top: 1130px;
    font-family: "Open Sans", sans-serif; font-size: 32px; letter-spacing: 2px; color: var(--paper);
  }
</style>
</head>
<body>
<main class="cover">
  <div class="cover-photo" role="img" aria-label="Photo of a businessman in an office chair with arms stretched wide, seen from behind, sitting in a green grass field under a bright blue sky with streaking white clouds"></div>

  <svg class="cover-art" viewBox="0 0 927 1200" aria-hidden="false">
    <rect class="flag-block" x="0" y="67" width="229" height="190"/>
    <rect class="flag-block" x="757" y="67" width="170" height="190"/>
    <text class="title-line title-line--harbor" x="268" y="237" font-size="150" textLength="470" lengthAdjust="spacingAndGlyphs">Harborlane</text>
    <text class="title-line title-line--venture" x="264" y="406" font-size="170" textLength="590" lengthAdjust="spacingAndGlyphs">Venture</text>
    <text class="title-line title-line--primer" x="266" y="518" font-size="112" textLength="584" lengthAdjust="spacingAndGlyphs">Primer 2014</text>
  </svg>

  <p class="blurb"><span class="blurb-lead">We start</span> from basic facts about life and culture and we go up to details of visa requirements, tax issues and the employment law. The audience is people excited about the prospects of moving to a new, up and coming place to start a new life.</p>
  <p class="author">Lucas</p>
</main>
</body>
</html>
```